English and Spanish Language School Needs a Business Card

Need a business card design a startup company called Corvelle Language School. The company will offer English and Spanish conversational level courses designed to make the learner feel comfortable with grammar and vocabulary. We would like to see a logo with some colour that should communicate learning, growth.

Target Market(s)

Consumers and businesses

Industry/Entity Type

Education

Contact Information for Business Card

TBD

Font styles to use
Serif

Requirements
Must have
• Include the following
• Logo
• Name
• Title
• Cellphone Number
• Office Phone number
• Email address
• Office Address

```html
<!DOCTYPE html>
<html lang="en">
<head>
<meta charset="utf-8">
<title>Corvelle Language School – Business Card</title>
<link rel="stylesheet" href="https://fonts.googleapis.com/css2?family=Montserrat:wght@400;500;600;700&display=swap">
<style>
  :root {
    --bg: #e9e6e2;
    --card-white: #ffffff;
    --card-dark: #1b2926;
    --brand-red: #cf2436;
    --brand-red-deep: #a9182a;
    --ink: #2a3230;
    --line-dark: #1e2b28;
    --paper-line: #ffffff;
  }
  * { box-sizing: border-box; margin: 0; padding: 0; }
  html, body { width: 1200px; height: 913px; overflow: hidden; }
  body {
    background: var(--bg);
    font-family: "Montserrat", sans-serif;
    display: flex;
    align-items: center;
    justify-content: center;
    gap: 40px;
  }
  .card {
    position: relative;
    width: 540px;
    height: 309px;
    border-radius: 14px;
    overflow: hidden;
    box-shadow: 0 8px 24px rgba(0,0,0,0.18);
  }
  .card__shape { position: absolute; inset: 0; width: 100%; height: 100%; }

  /* Front */
  .card--front { background: var(--card-white); }
  .holder {
    position: absolute; top: 58px; right: 44px; text-align: right;
  }
  .holder__name { font-size: 19px; font-weight: 600; color: var(--ink); letter-spacing: 0.3px; }
  .holder__title { font-size: 11px; font-weight: 400; color: var(--ink); margin-top: 2px; }
  .holder__dot {
    position: absolute; top: 52px; right: -14px;
    width: 28px; height: 28px; border-radius: 50%; background: var(--brand-red);
  }
  .brand { position: absolute; color: var(--brand-red); font-weight: 700; line-height: 1; }
  .brand__name { display: block; }
  .brand__sub { display: block; font-weight: 700; }
  .card--front .brand { left: 30px; top: 110px; }
  .card--front .brand__name { font-size: 42px; letter-spacing: -1px; }
  .card--front .brand__sub { font-size: 13px; margin-top: 4px; margin-left: 4px; }

  .contact {
    position: absolute; left: 32px; top: 184px;
    list-style: none; color: var(--brand-red); font-size: 12.5px; line-height: 17px;
  }
  .contact__row { display: flex; align-items: center; gap: 8px; }
  .contact__icon { width: 11px; height: 11px; flex: none; }
  .contact__row--plain { padding-left: 0; }
  .contact__row--web { font-weight: 700; }

  /* Back */
  .card--back { background: var(--card-dark); }
  .card--back .brand { left: 190px; top: 104px; }
  .card--back .brand__name { font-size: 58px; letter-spacing: -1.5px; }
  .card--back .brand__sub { font-size: 17px; margin-top: 4px; margin-left: 6px; }
  .web {
    position: absolute; left: 34px; bottom: 16px;
    color: #ffffff; font-size: 13px; font-weight: 500; letter-spacing: 0.3px;
  }
</style>
</head>
<body>

  <section class="card card--front" aria-label="Business card front">
    <svg class="card__shape" viewBox="0 0 540 309" preserveAspectRatio="none" aria-hidden="true">
      <path d="M0,309 L0,300 C200,299 300,288 380,220 C440,160 480,128 540,122 L540,309 Z" fill="var(--brand-red)"/>
      <path d="M0,296 C200,295 300,284 380,216 C440,156 480,124 540,118" fill="none" stroke="var(--line-dark)" stroke-width="4"/>
    </svg>

    <div class="holder">
      <p class="holder__name">Marten Aldous</p>
      <p class="holder__title">Director</p>
    </div>
    <span class="holder__dot" aria-hidden="true"></span>

    <div class="brand">
      <span class="brand__name">Corvelle</span>
      <span class="brand__sub">Language School</span>
    </div>

    <ul class="contact">
      <li class="contact__row">Po Box 218</li>
      <li class="contact__row">Halloway VIC 3902</li>
      <li class="contact__row">
        <svg class="contact__icon" viewBox="0 0 12 12" aria-hidden="true"><rect x="3" y="0.5" width="6" height="11" rx="1" fill="none" stroke="var(--ink)" stroke-width="1.2"/><circle cx="6" cy="9.5" r="0.8" fill="var(--ink)"/></svg>
        +330 2417-8830
      </li>
      <li class="contact__row">
        <svg class="contact__icon" viewBox="0 0 12 12" aria-hidden="true"><path d="M2.5,1 L4.5,1 L5.5,3.5 L4,4.8 C4.7,6.4 5.6,7.3 7.2,8 L8.5,6.5 L11,7.5 L11,9.5 C11,10.3 10.3,11 9.5,11 C5,10.7 1.3,7 1,2.5 C1,1.7 1.7,1 2.5,1 Z" fill="var(--ink)"/></svg>
        +330 2419-6052
      </li>
      <li class="contact__row">
        <svg class="contact__icon" viewBox="0 0 12 12" aria-hidden="true"><rect x="0.8" y="2.3" width="10.4" height="7.4" rx="1" fill="none" stroke="var(--ink)" stroke-width="1.2"/><path d="M1,2.8 L6,6.6 L11,2.8" fill="none" stroke="var(--ink)" stroke-width="1.2"/></svg>
        hello@corvelleschool.com
      </li>
      <li class="contact__row contact__row--web">
        <svg class="contact__icon" viewBox="0 0 12 12" aria-hidden="true"><circle cx="6" cy="6" r="5" fill="none" stroke="var(--ink)" stroke-width="1.1"/><path d="M1,6 H11 M6,1 C3.5,3.5 3.5,8.5 6,11 M6,1 C8.5,3.5 8.5,8.5 6,11" fill="none" stroke="var(--ink)" stroke-width="0.9"/></svg>
        corvelleschool.com
      </li>
    </ul>
  </section>

  <section class="card card--back" aria-label="Business card back">
    <svg class="card__shape" viewBox="0 0 540 309" preserveAspectRatio="none" aria-hidden="true">
      <path d="M0,309 L0,276 C120,270 230,250 320,205 C410,160 470,150 540,148 L540,309 Z" fill="var(--paper-line)"/>
      <path d="M0,309 L0,283 C120,277 230,257 320,212 C410,167 470,157 540,155 L540,309 Z" fill="var(--brand-red)"/>
      <path d="M0,309 L0,300 C140,300 300,280 540,250 L540,309 Z" fill="var(--brand-red-deep)" opacity="0.35"/>
    </svg>

    <div class="brand">
      <span class="brand__name">Corvelle</span>
      <span class="brand__sub">Language School</span>
    </div>

    <p class="web">www.corvelleschool.com</p>
  </section>

</body>
</html>
```